Post card

I want an educational customer postcard with our logo, email, and contact number. We are a residential foundation inspection & repair company here in Los Angeles. We provide foundation repair, earthquake retrofitting, and reinforcement.
Our number is 323-555-0148.
Email info@bramblecrestworks.com
Our license number is #2839165

OUR GOAL
Our primary objective is to empower clients with comprehensive knowledge about foundation issues and earthquake retrofitting. By educating them on the potential risks associated with foundation problems and the importance of earthquake retrofitting, we aim to equip homeowners with the necessary information to make informed decisions about safeguarding their properties. Highlighting the benefits of having their houses properly bolted not only enhances structural integrity but also provides peace of mind during seismic events, ensuring the safety and security of their homes and loved ones.

```html
<!DOCTYPE html>
<html lang="en">
<head>
<meta charset="utf-8">
<title>Bramblecrest Works – Postcard</title>
<link href="https://fonts.googleapis.com/css2?family=Montserrat:wght@500;600;700;800;900&display=swap" rel="stylesheet">
<style>
  :root {
    --brand-blue: #1466f5;
    --brand-red: #d0101e;
    --ink: #111111;
    --paper: #ffffff;
    --backdrop: #1b1b1b;
    --rule-grey: #9a9a9a;
    --stamp-grey: #d2d2d2;
  }
  html, body {
    margin: 0;
    width: 736px;
    height: 1200px;
    overflow: hidden;
    background: var(--backdrop);
  }
  .sheet {
    width: 736px;
    height: 1200px;
    display: flex;
    flex-direction: column;
    align-items: center;
    justify-content: center;
    gap: 40px;
  }
  .postcard {
    display: block;
    width: 640px;
    height: 426px;
    filter: drop-shadow(0 10px 18px rgba(0,0,0,.55));
  }
  .postcard text { font-family: 'Montserrat', sans-serif; }
  .headline { font-weight: 900; font-size: 50px; }
  .brand-name { font-weight: 800; fill: var(--brand-blue); }
  .license { font-weight: 700; fill: var(--ink); }
  .provide-title { font-weight: 800; font-size: 36px; fill: var(--ink); }
  .provide-item { font-weight: 700; font-size: 34px; fill: var(--brand-red); }
  .phone { font-weight: 900; fill: var(--paper); }
  .contact { font-weight: 700; fill: var(--paper); }
  .about-title { font-weight: 800; font-size: 28px; fill: var(--paper); }
  .about-copy { font-weight: 500; font-size: 15.5px; fill: var(--paper); }
  .services-title { font-weight: 800; font-size: 36px; fill: var(--paper); }
  .service-item { font-weight: 700; font-size: 24px; fill: var(--paper); }
  .tick { fill: none; stroke-width: 2.4; stroke-linecap: round; stroke-linejoin: round; }
</style>
</head>
<body>
<main class="sheet">

  <!-- Front side -->
  <svg class="postcard postcard--front" viewBox="0 0 1076 716" xmlns="http://www.w3.org/2000/svg">
    <defs>
      <linearGradient id="houseTones" x1="0" y1="0" x2="0" y2="1">
        <stop offset="0" stop-color="#b9d6f1"/>
        <stop offset="0.3" stop-color="#d8e6f0"/>
        <stop offset="0.55" stop-color="#a98462"/>
        <stop offset="0.85" stop-color="#3c3c42"/>
        <stop offset="1" stop-color="#6f8f45"/>
      </linearGradient>
    </defs>
    <rect class="card-base" width="1076" height="716" fill="var(--paper)"/>
    <polygon class="house-photo" role="img" aria-label="Photo of a modern two-storey house with large windows under a blue sky"
             points="465,0 1076,0 1076,716 550,716 540,400" fill="url(#houseTones)"/>
    <path class="bolt-stripe" d="M0,201 H396 V318 L530,395 L478,18 L592,38 V199 H1076"
          fill="none" stroke="var(--brand-blue)" stroke-width="36" stroke-linejoin="miter"/>

    <text class="headline" x="1040" y="72" text-anchor="end" fill="var(--brand-red)">RESIDENTIAL</text>
    <text class="headline" x="1040" y="115" text-anchor="end" fill="var(--paper)">SEISMIC</text>
    <text class="headline" x="1040" y="158" text-anchor="end" fill="var(--brand-red)">RETROFIT</text>

    <g class="brand">
      <rect x="67" y="44" width="62" height="62" fill="var(--brand-blue)"/>
      <text class="brand-name" x="145" y="72" font-size="34">BRAMBLECREST</text>
      <text class="brand-name" x="145" y="108" font-size="34">WORKS</text>
      <text class="license" x="395" y="156" font-size="11" text-anchor="end">#2839165</text>
    </g>

    <text class="provide-title" x="68" y="300">WE PROVIDE :</text>
    <g class="provide-list">
      <path class="tick" stroke="var(--brand-blue)" d="M88,340 h-18 v22 h22 v-10 M76,350 l6,6 l12,-14"/>
      <text class="provide-item" x="113" y="362">Foundation</text>
      <text class="provide-item" x="113" y="390">Repair</text>
      <line x1="113" y1="401" x2="326" y2="401" stroke="var(--brand-red)" stroke-width="1.5"/>
      <path class="tick" stroke="var(--brand-blue)" d="M88,413 h-18 v22 h22 v-10 M76,423 l6,6 l12,-14"/>
      <text class="provide-item" x="113" y="433">Earthquake</text>
      <text class="provide-item" x="113" y="470">Retrofitting</text>
      <line x1="113" y1="481" x2="326" y2="481" stroke="var(--brand-red)" stroke-width="1.5"/>
      <path class="tick" stroke="var(--brand-blue)" d="M88,497 h-18 v22 h22 v-10 M76,507 l6,6 l12,-14"/>
      <text class="provide-item" x="113" y="518">Reinforcement</text>
    </g>

    <polygon class="phone-band" points="0,575 530,575 552,716 0,716" fill="var(--brand-red)"/>
    <circle cx="81" cy="652" r="22" fill="var(--ink)"/>
    <path d="M73,641 q-2,2 0,8 q5,10 14,14 q5,2 7,-1 l2,-3 l-6,-4 l-3,3 q-6,-3 -9,-9 l3,-3 l-4,-6 z" fill="var(--paper)"/>
    <text class="phone" x="113" y="676" font-size="60">323-555-0148</text>

    <polygon class="email-band" points="606,630 1076,630 1076,716 590,716" fill="var(--brand-blue)"/>
    <circle cx="654" cy="668" r="12" fill="var(--ink)"/>
    <rect x="647" y="663" width="14" height="10" fill="none" stroke="var(--paper)" stroke-width="1.6"/>
    <path d="M647,663 l7,6 l7,-6" fill="none" stroke="var(--paper)" stroke-width="1.6"/>
    <text class="contact" x="678" y="674" font-size="20" textLength="370" lengthAdjust="spacingAndGlyphs">INFO@BRAMBLECRESTWORKS.COM</text>
    <text class="contact" x="678" y="701" font-size="20">#2839165</text>
  </svg>

  <!-- Back side -->
  <svg class="postcard postcard--back" viewBox="0 0 1076 716" xmlns="http://www.w3.org/2000/svg">
    <defs>
      <linearGradient id="aboutTones" x1="0" y1="0" x2="1" y2="1">
        <stop offset="0" stop-color="#1a5fef"/>
        <stop offset="0.6" stop-color="#2a78f8"/>
        <stop offset="1" stop-color="#1660f2"/>
      </linearGradient>
    </defs>
    <rect class="card-base" width="1076" height="716" fill="var(--paper)"/>
    <polygon class="about-panel" role="img" aria-label="Blue-tinted photo of a house behind the about text"
             points="0,0 552,0 640,575 0,575" fill="url(#aboutTones)"/>
    <polygon class="contact-band" points="0,575 640,575 660,716 0,716" fill="var(--brand-red)"/>

    <text class="about-title" x="60" y="52" textLength="470" lengthAdjust="spacingAndGlyphs">ABOUT BRAMBLECREST WORKS</text>
    <g class="about-copy-block">
      <text class="about-copy" x="60" y="94">BRAMBLECREST WORKS is a company born out of a</text>
      <text class="about-copy" x="60" y="115">passion for making California a safer place. With our</text>
      <text class="about-copy" x="60" y="136">expertise in earthquake retrofitting and our hard-</text>
      <text class="about-copy" x="60" y="157">working team, we have been reinforcing older homes</text>
      <text class="about-copy" x="60" y="178">up to current code all over California.</text>
    </g>

    <text class="services-title" x="59" y="256">SERVICES</text>
    <g class="service-list">
      <g transform="translate(0,0)"><path class="tick" stroke="var(--paper)" stroke-width="1.8" d="M74,284 h-11 v13 h13 v-6 M66,290 l4,4 l8,-9"/><text class="service-item" x="93" y="300">INSPECTIONS</text></g>
      <g transform="translate(0,33)"><path class="tick" stroke="var(--paper)" stroke-width="1.8" d="M74,284 h-11 v13 h13 v-6 M66,290 l4,4 l8,-9"/><text class="service-item" x="93" y="300">HOUSE BOLTING</text></g>
      <g transform="translate(0,66)"><path class="tick" stroke="var(--paper)" stroke-width="1.8" d="M74,284 h-11 v13 h13 v-6 M66,290 l4,4 l8,-9"/><text class="service-item" x="93" y="300">CRACK REPAIR</text></g>
      <g transform="translate(0,99)"><path class="tick" stroke="var(--paper)" stroke-width="1.8" d="M74,284 h-11 v13 h13 v-6 M66,290 l4,4 l8,-9"/><text class="service-item" x="93" y="300">BEAM REINFORCEMENT</text></g>
      <g transform="translate(0,132)"><path class="tick" stroke="var(--paper)" stroke-width="1.8" d="M74,284 h-11 v13 h13 v-6 M66,290 l4,4 l8,-9"/><text class="service-item" x="93" y="300">STRUCTURAL DEFECTS</text></g>
      <g transform="translate(0,165)"><path class="tick" stroke="var(--paper)" stroke-width="1.8" d="M74,284 h-11 v13 h13 v-6 M66,290 l4,4 l8,-9"/><text class="service-item" x="93" y="300">CRIPPLE WALL BRACING</text></g>
      <g transform="translate(0,198)"><path class="tick" stroke="var(--paper)" stroke-width="1.8" d="M74,284 h-11 v13 h13 v-6 M66,290 l4,4 l8,-9"/><text class="service-item" x="93" y="300">FOUNDATION CRACK STITCHING</text></g>
      <g transform="translate(0,231)"><path class="tick" stroke="var(--paper)" stroke-width="1.8" d="M74,284 h-11 v13 h13 v-6 M66,290 l4,4 l8,-9"/><text class="service-item" x="93" y="300">CRAWL SPACE ENCAPSULATION</text></g>
    </g>

    <circle cx="74" cy="625" r="13" fill="var(--ink)"/>
    <path d="M69,618 q-1,1 0,5 q3,6 8,8 q3,1 4,-1 l1,-2 l-4,-2 l-2,2 q-3,-2 -5,-5 l2,-2 l-2,-3 z" fill="var(--paper)"/>
    <text class="phone" x="98" y="640" font-size="42">323-555-0148</text>
    <circle cx="74" cy="665" r="12" fill="var(--ink)"/>
    <rect x="67" y="660" width="14" height="10" fill="none" stroke="var(--paper)" stroke-width="1.6"/>
    <path d="M67,660 l7,6 l7,-6" fill="none" stroke="var(--paper)" stroke-width="1.6"/>
    <text class="contact" x="98" y="673" font-size="22">INFO@BRAMBLECRESTWORKS.COM</text>
    <text class="contact" x="98" y="700" font-size="22">#2839165</text>

    <g class="brand">
      <rect x="630" y="40" width="44" height="44" fill="var(--brand-blue)"/>
      <text class="brand-name" x="688" y="60" font-size="24">BRAMBLECREST</text>
      <text class="brand-name" x="688" y="86" font-size="24">WORKS</text>
      <text class="license" x="853" y="112" font-size="8" text-anchor="end">#2839165</text>
    </g>
    <rect class="stamp-box" x="955" y="35" width="80" height="80" fill="var(--stamp-grey)"/>
    <g class="address-lines" stroke="var(--rule-grey)" stroke-width="1.5">
      <line x1="644" y1="235" x2="1024" y2="235"/>
      <line x1="644" y1="293" x2="1024" y2="293"/>
      <line x1="644" y1="350" x2="1024" y2="350"/>
    </g>
    <path class="bolt-stripe" d="M640,585 H760 L812,698 L800,472 L878,505 V585 H1076"
          fill="none" stroke="var(--brand-blue)" stroke-width="20" stroke-linejoin="miter"/>
  </svg>

</main>
</body>
</html>
```